Business card design for crowd sourced review site.

I need a business card magnet design for an online, crowd-sourced, restaurant review site strictly for Kosher restaurants.
It is similar to WanderNotes but catering to a very particular crowd.
The markets it will be distributed in are flooded with business card fridge magnets so this needs to be eye-catching and unique. The Business name is PlateRanker
The website isnt finished but you can see the basic setup here
http://dining.brevtalo.com/

The second image i included is another logo design I liked and was thinking about using and decided I will probably also make a SECOND custom cut business card in the shape of that icon. Bonus if you can throw that in also.

Target Market(s)

Jewish consumers aged 20-35

Industry/Entity Type

Business

Contact Information for Business Card

see description.
Design should not be too crowded and should in eye-catching. Will mainly be used as fridge magnets.

Requirements
Must have
• Website address. logo.
Nice to have
• tagline. (Honest Reviews of Kosher Restaurants from Real Local Diners)
• Im not a professional but I personally think the color blue goes along with this concept. ill leave it to you to decide.
Should not have
• any religious symbols.

```html
<!DOCTYPE html>
<html lang="en">
<head>
<meta charset="utf-8">
<title>PlateRanker Business Card</title>
<link href="https://fonts.googleapis.com/css2?family=Montserrat:wght@400;500;600;700&display=swap" rel="stylesheet">
<style>
  :root {
    --stage: #2a2a2a;
    --card-black: #060606;
    --card-white: #ffffff;
    --accent-red: #e23a27;
    --ink: #1b1b1b;
    --ink-soft: #333333;
  }
  * { box-sizing: border-box; margin: 0; padding: 0; }
  html, body { width: 1200px; height: 1000px; overflow: hidden; }
  body {
    background: var(--stage);
    font-family: "Montserrat", Arial, sans-serif;
    position: relative;
  }
  .card {
    position: absolute;
    width: 525px;
    height: 300px;
    border-radius: 18px;
    overflow: hidden;
  }
  .card-front {
    left: 150px; top: 150px;
    background: var(--card-black);
    display: flex; align-items: center; justify-content: center; gap: 14px;
  }
  .front-mark {
    width: 26px; height: 26px; border-radius: 50%;
    background: var(--accent-red);
  }
  .front-name {
    color: var(--card-white);
    font-size: 46px; font-weight: 700; letter-spacing: 0.5px;
  }
  .card-back {
    left: 525px; top: 540px;
    background: var(--card-white);
  }
  .card-back svg.frame { position: absolute; left: 0; top: 0; }
  .back-name {
    position: absolute; left: 200px; top: 26px;
    font-size: 30px; font-weight: 700; color: var(--ink);
  }
  .person {
    position: absolute; left: 250px; top: 74px;
  }
  .person-name { font-size: 18px; font-weight: 600; color: var(--accent-red); line-height: 1.1; }
  .person-role { font-size: 11px; color: var(--ink-soft); margin-top: 2px; }
  .logo-spot {
    position: absolute; left: 125px; top: 152px;
    width: 64px; height: 64px; border-radius: 50%;
    background: var(--accent-red);
  }
  .contacts {
    position: absolute; left: 262px; top: 143px;
    list-style: none;
  }
  .contacts li {
    display: flex; align-items: center; gap: 8px;
    font-size: 12px; color: var(--ink); height: 22px;
  }
  .contacts svg { width: 10px; height: 10px; fill: var(--accent-red); flex: none; }
  .tagline {
    position: absolute; left: 22px; right: 20px; top: 264px;
    font-size: 12.5px; font-weight: 700; color: var(--accent-red);
    text-transform: uppercase; letter-spacing: 0.2px; white-space: nowrap;
  }
</style>
</head>
<body>
  <section class="card card-front">
    <span class="front-mark"></span>
    <span class="front-name">PlateRanker</span>
  </section>

  <section class="card card-back">
    <svg class="frame" width="525" height="300" viewBox="0 0 525 300">
      <line x1="330" y1="22" x2="525" y2="22" stroke="var(--accent-red)" stroke-width="2"/>
      <polygon points="0,128 96,128 56,242 0,242" fill="var(--accent-red)"/>
      <line x1="96" y1="128" x2="525" y2="128" stroke="var(--accent-red)" stroke-width="2"/>
      <line x1="56" y1="242" x2="525" y2="242" stroke="var(--accent-red)" stroke-width="2"/>
    </svg>
    <div class="back-name">PlateRanker</div>
    <div class="person">
      <div class="person-name">Marlo Pennick</div>
      <div class="person-role">Director</div>
    </div>
    <div class="logo-spot"></div>
    <ul class="contacts">
      <li><svg viewBox="0 0 10 10"><path d="M2 0.5l2 2-1 1.2c.6 1.3 1.7 2.4 3 3l1.2-1 2 2-1.2 1.8C4.5 9.5.5 5.5.3 1.7z"/></svg>+330 5180-2294</li>
      <li><svg viewBox="0 0 10 10"><path d="M0 2h10v6H0z M0 2l5 3.5L10 2" stroke="#fff" stroke-width="0.8"/></svg>info@dining.brevtalo.com</li>
      <li><svg viewBox="0 0 10 10"><circle cx="5" cy="5" r="4.6"/><path d="M0.5 5h9M5 .5c-2 2.5-2 6.5 0 9M5 .5c2 2.5 2 6.5 0 9" stroke="#fff" stroke-width="0.7" fill="none"/></svg>www.dining.brevtalo.com</li>
    </ul>
    <div class="tagline">Honest Reviews of Kosher Restaurants from Real Local Diners</div>
  </section>
</body>
</html>
```